Fernlow - telephone directory add

We need simple artwork advertisement for insertion in a local yellow pages telephone directory
Design brief for telephone ads
This project is to provide a pair of 62mm high x 91mm wide ‘yellow page adds’ for our company to place in a local phone book.
• They should reflect the same theme
• They should be based on a white ‘knock out’ background (printed on yellow paper) and have one colour in addition to black.
• Fernlow is our trading name
• Main contact details are www.Fernlow-demo.gg, telephone 473518, sales@fernlow, facebook.com/fernlowmotorimports
• Our address is Varclette Lane, St Sampson, GY5 8QT
• First box
o Vehicle sales – (we would like to promote)
 Japanese Minivan specialist
 European & UK vehicles supplied at best prices
 Vans and light commercials available
 Trusted supplier with 20 years experience

• Second box
o Service and repairs to all models
 Popular £99 service health check
 Qualified mechanics
 Wheel alignment & Air conditioning
 Fleet servicing options

local readers

Automotive

• Design brief for telephone ads
• This project is to provide a pair of 62mm high x 91mm wide ‘yellow page adds’ for our company to place in a local phone book.
• • They should reflect the same theme
• • They should be based on a white ‘knock out’ background (printed on yellow paper) and have one colour in addition to black.
• • Fernlow is our trading name
• • Main contact details are www.Fernlow-demo.gg, telephone 473518, sales@fernlow, facebook.com/fernlowmotorimports
• • Our address is Varclette Lane, St Sampson, GY5 8QT
• • First box
• o Vehicle sales – (we would like to promote)
•  Japanese Minivan specialist
•  European & UK vehicles supplied at best prices
•  Vans and light commercials available
•  Trusted supplier with 20 years experience
• • Second box
• o Service and repairs to all models
•  Popular £99 service health check
•  Qualified mechanics
•  Wheel alignment & Air conditioning
•  Fleet servicing options
• see attached word doc
• • First box
• • Second box
•  Qualified mechanics

```html
<!DOCTYPE html>
<html lang="en">
<head>
<meta charset="utf-8">
<title>Fernlow – Vehicle Sales directory advert</title>
<link href="https://fonts.googleapis.com/css2?family=Montserrat:wght@700;800;900&family=Open+Sans:wght@600;700&display=swap" rel="stylesheet">
<style>
  :root{
    --page-yellow:#f6e67c;
    --brand-red:#e82127;
    --ink:#231f20;
    --paper:#ffffff;
  }
  *{margin:0;padding:0;box-sizing:border-box}
  html,body{width:1200px;height:1047px;overflow:hidden;background:var(--page-yellow)}
  .canvas{position:relative;width:1200px;height:1047px;background:var(--page-yellow)}
  .advert{position:absolute;left:66px;top:158px;width:1069px;height:728px;background:var(--paper);overflow:hidden;font-family:"Montserrat",sans-serif}
  .headline-band{position:absolute;left:0;top:0;width:100%;height:216px;background:var(--brand-red)}
  .headline-rule{position:absolute;left:0;top:216px;width:100%;height:10px;background:var(--ink)}
  .web-tab{position:absolute;left:0;top:236px;width:470px;height:54px;background:var(--ink);clip-path:polygon(0 0,100% 0,97% 100%,0 100%)}
  .web-address{position:absolute;left:56px;top:4px;font-family:"Open Sans",sans-serif;font-weight:700;font-size:35px;color:var(--paper);line-height:46px}
  .headline{position:absolute;left:52px;top:14px;color:var(--paper);font-weight:900;line-height:.86;text-shadow:-4px 4px 0 var(--ink)}
  .headline span{display:block}
  .headline .line-1{font-size:92px;letter-spacing:-1px}
  .headline .line-2{font-size:118px;letter-spacing:-2px;margin-top:6px}
  .hero-vehicle{position:absolute;left:482px;top:18px;width:544px;height:304px;border-radius:46% 40% 30% 30% / 50% 45% 30% 30%;background:radial-gradient(ellipse at 45% 55%,#ffffff 0%,#e6e6e6 55%,#9a9a9a 100%)}
  .claim{position:absolute;left:0;width:100%;text-align:center;font-weight:800;line-height:1}
  .claim-lead{top:322px;font-size:47px;color:var(--ink);letter-spacing:.5px}
  .claim-main{top:362px;font-size:66px;color:var(--brand-red);letter-spacing:1px}
  .offer{position:absolute;top:434px;width:302px;text-align:center}
  .offer-minivan{left:30px}.offer-european{left:382px}.offer-vans{left:735px}
  .offer-photo{margin:0 auto;width:176px;height:80px;border-radius:38% 30% 18% 18% / 45% 45% 20% 20%;background:linear-gradient(180deg,#f4f4f4 0%,#cfcfcf 70%,#6d6d6d 100%)}
  .offer-title{margin-top:8px;height:59px;font-weight:800;font-size:29px;line-height:29px;color:var(--brand-red);white-space:nowrap}
  .offer-tag{display:block;margin-top:0;height:28px;background:var(--ink);color:var(--paper);font-weight:800;font-size:20px;line-height:29px;letter-spacing:.5px}
  .divider{position:absolute;top:446px;width:1.5px;height:160px;background:#7a7a7a}
  .divider-1{left:356px}.divider-2{left:711px}
  .contact-row{position:absolute;top:624px;left:0;width:100%;display:flex;justify-content:center;gap:34px;align-items:center}
  .contact-item{display:flex;align-items:center;gap:6px;font-family:"Open Sans",sans-serif;font-weight:700;font-size:38px;color:var(--brand-red);line-height:40px}
  .contact-item svg{width:34px;height:34px;flex:none}
  .address-bar{position:absolute;left:0;top:676px;width:100%;height:52px;background:var(--ink);display:flex;align-items:center;justify-content:center;gap:8px;color:var(--paper);font-family:"Open Sans",sans-serif;font-weight:700;font-size:28px;letter-spacing:1px}
  .address-bar svg{width:30px;height:30px}
</style>
</head>
<body>
<div class="canvas">
  <section class="advert">
    <div class="headline-band"></div>
    <div class="headline-rule"></div>
    <h1 class="headline"><span class="line-1">VEHICLE</span><span class="line-2">SALES</span></h1>
    <div class="web-tab"><span class="web-address">www.Fernlow-demo.gg</span></div>
    <div class="hero-vehicle" role="img" aria-label="Photo of a white SUV, front three-quarter view"></div>

    <p class="claim claim-lead">TRUSTED SUPPLIER WITH</p>
    <p class="claim claim-main">20 YEARS EXPERIENCE</p>

    <div class="offer offer-minivan">
      <div class="offer-photo" role="img" aria-label="Photo of a white Japanese minivan"></div>
      <h2 class="offer-title">JAPANESE<br>MINIVAN</h2>
      <span class="offer-tag">SPECIALIST</span>
    </div>
    <div class="divider divider-1"></div>
    <div class="offer offer-european">
      <div class="offer-photo" role="img" aria-label="Photo of a silver European SUV"></div>
      <h2 class="offer-title">EUROPEAN &amp; UK<br>VEHICLES</h2>
      <span class="offer-tag">SUPPLIED AT BEST PRICES</span>
    </div>
    <div class="divider divider-2"></div>
    <div class="offer offer-vans">
      <div class="offer-photo" role="img" aria-label="Photo of a white panel van"></div>
      <h2 class="offer-title">VANS AND LIGHT<br>COMMERCIALS</h2>
      <span class="offer-tag">AVAILABLE</span>
    </div>

    <div class="contact-row">
      <span class="contact-item">
        <svg viewBox="0 0 34 34" aria-hidden="true"><circle cx="17" cy="17" r="15" fill="none" stroke="#231f20" stroke-width="2.5"/><path d="M11.5 9.5l3.5-1 2 4.5-2 1.5c.8 2.2 2.3 3.8 4.5 4.7l1.6-2 4.4 2.1-1 3.4c-6.6.4-13.4-6.4-13-13.2z" fill="#231f20"/></svg>
        473518
      </span>
      <span class="contact-item">
        <svg viewBox="0 0 34 34" aria-hidden="true"><circle cx="17" cy="17" r="15" fill="none" stroke="#231f20" stroke-width="2.5"/><rect x="9" y="11.5" width="16" height="11" fill="none" stroke="#231f20" stroke-width="1.8"/><path d="M9 11.5l8 6.5 8-6.5M9 22.5l6-5.5M25 22.5l-6-5.5" fill="none" stroke="#231f20" stroke-width="1.5"/></svg>
        sales@fernlow
      </span>
    </div>

    <footer class="address-bar">
      <svg viewBox="0 0 30 30" aria-hidden="true"><circle cx="15" cy="15" r="13.5" fill="none" stroke="#fff" stroke-width="2"/><path d="M15 24c-4-5-6-8-6-11a6 6 0 0 1 12 0c0 3-2 6-6 11z" fill="none" stroke="#fff" stroke-width="2"/><circle cx="15" cy="13" r="2.2" fill="#fff"/></svg>
      VARCLETTE LANE, ST SAMPSON, GY5 8QT
    </footer>
  </section>
</div>
</body>
</html>
```